Flyer Design for Norvane LLC

We need a Flyer for a new company called “Norvane LLC”. This is a technology process improvement company providing a comprehensive assessment of the technology used to run their business. The documentation and review process delivers the visibility and reassurance they need to protect their business and plan for the future. The product is called “Systems Pathcharting”. Our primary target is small-medium size businesses, with the deliverables going to the decision maker.

We would like to see the designs use the color blue. Our tag line is "Protect Your Business · Take Control of IT".

- Attached: Norvane LLC Overview document we put together as a starting point. Use as much or as little as you wish.
- Attached: Business Card and Logo designs for colors, etc.

Industry/Entity Type

It Company

```html
<!DOCTYPE html>
<html lang="en">
<head>
<meta charset="utf-8">
<title>Systems Pathcharting – Norvane LLC</title>
<link rel="stylesheet" href="https://fonts.googleapis.com/css2?family=Crimson+Pro:wght@400;600;700&display=swap">
<style>
  :root {
    --brand-blue: #1a74b9;
    --title-blue: #1f74b8;
    --band-dark: #4a4b4d;
    --panel-grey: #808285;
    --hub-grey: #8d8e90;
    --page-bg: #e6e6e6;
    --white: #ffffff;
  }
  * { margin: 0; padding: 0; box-sizing: border-box; }
  html, body { width: 1200px; height: 1200px; overflow: hidden; }
  body {
    background: var(--page-bg);
    font-family: "Crimson Pro", "Palatino Linotype", serif;
    position: relative;
  }
  .flyer {
    position: absolute;
    left: 197px; top: 78px;
    width: 806px; height: 1044px;
    background: var(--white);
    overflow: hidden;
    box-shadow: 0 1px 4px rgba(0,0,0,0.12);
  }
  .brand {
    position: absolute;
    left: 28px; top: 72px;
    display: flex; align-items: center; gap: 10px;
  }
  .brand-mark {
    width: 26px; height: 26px;
    background: var(--brand-blue);
  }
  .brand-name {
    font-size: 30px; font-weight: 700;
    color: var(--brand-blue);
    letter-spacing: 0.5px;
  }
  .title {
    position: absolute;
    left: 300px; top: 14px;
    width: 420px;
    text-align: center;
    color: var(--title-blue);
    font-weight: 700;
    font-size: 62px;
    line-height: 66px;
    letter-spacing: 1px;
    white-space: nowrap;
  }
  .title sup { font-size: 40px; vertical-align: 18px; }
  .tagline-band {
    position: absolute;
    left: 0; top: 155px; width: 100%; height: 47px;
    background: var(--band-dark);
    color: var(--white);
    font-size: 28px;
    text-align: center;
    line-height: 47px;
    letter-spacing: 0.5px;
    z-index: 2;
  }
  .photo {
    position: absolute;
    left: 0; top: 202px; width: 100%; height: 476px;
    background: linear-gradient(180deg, #b9b6b3 0%, #c9c7c4 45%, #d7d6d4 100%);
  }
  .info-panel {
    position: absolute;
    left: 347px; top: 586px; width: 437px; height: 364px;
    background: var(--panel-grey);
  }
  .diagram { position: absolute; left: 0; top: 0; width: 806px; height: 1044px; }
  .intro-box {
    position: absolute;
    left: 23px; top: 417px; width: 309px; height: 533px;
    background: var(--brand-blue);
    color: var(--white);
    padding: 18px 18px 0 20px;
  }
  .intro-box h2 { font-size: 19px; font-weight: 700; margin-bottom: 10px; }
  .intro-box p { font-size: 17px; line-height: 19px; margin-bottom: 13px; }
  .intro-box hr { border: 0; border-top: 1px solid rgba(255,255,255,0.75); width: 262px; margin: 2px 0 20px; }
  .deliverables-head {
    position: absolute;
    left: 347px; top: 822px; width: 437px; height: 23px;
    background: var(--brand-blue);
    color: var(--white);
    text-align: center;
    font-size: 18px; font-weight: 700; line-height: 23px;
  }
  .deliverables {
    position: absolute;
    left: 359px; top: 851px; width: 420px;
    display: grid; grid-template-columns: 211px 1fr;
    row-gap: 2px;
    list-style: none;
    color: var(--white);
    font-size: 12.5px; font-weight: 600; line-height: 19px;
  }
  .deliverables li::before { content: "• "; }
  .cta {
    position: absolute;
    left: 0; top: 955px; width: 100%;
    text-align: center;
    color: var(--title-blue);
    font-size: 30px; font-weight: 700;
  }
  .contact-band {
    position: absolute;
    left: 0; top: 997px; width: 100%; height: 47px;
    background: var(--brand-blue);
    color: var(--white);
    text-align: center;
    font-size: 16px; line-height: 47px;
  }
  .contact-band strong { font-weight: 700; }
  .contact-band .sep { margin: 0 6px; }
  .node-label { font-family: "Crimson Pro", serif; font-weight: 700; font-size: 13px; fill: var(--brand-blue); text-anchor: middle; }
  .hub-label { font-family: "Crimson Pro", serif; font-weight: 700; font-size: 18px; fill: var(--white); text-anchor: middle; }
  .icon { fill: none; stroke: var(--brand-blue); stroke-width: 2; stroke-linejoin: round; stroke-linecap: round; }
</style>
</head>
<body>
  <div class="flyer">
    <div class="brand">
      <span class="brand-mark"></span>
      <span class="brand-name">Norvane LLC</span>
    </div>
    <h1 class="title">SYSTEMS<br>PATHCHARTING<sup>™</sup></h1>
    <div class="tagline-band">PROTECT YOUR BUSINESS • TAKE CONTROL OF IT</div>

    <div class="photo" role="img" aria-label="Photo of a business team meeting and shaking hands in a bright glass-walled office"></div>
    <div class="info-panel"></div>

    <svg class="diagram" viewBox="0 0 806 1044" aria-label="Evaluating five functional areas">
      <circle cx="565" cy="622" r="118" fill="var(--hub-grey)" stroke="var(--brand-blue)" stroke-width="14"/>
      <text class="hub-label" x="565" y="606">Evaluating</text>
      <text class="hub-label" x="565" y="628">Five Functional</text>
      <text class="hub-label" x="565" y="650">Areas</text>

      <g>
        <circle cx="569" cy="482" r="56" fill="var(--white)" stroke="var(--brand-blue)" stroke-width="7"/>
        <path d="M612 510 L630 525 L605 520 Z" fill="var(--white)"/>
        <text class="node-label" x="569" y="458">IT Service</text>
        <text class="node-label" x="569" y="473">Delivery</text>
        <rect class="icon" x="549" y="486" width="38" height="24" rx="2"/>
        <path class="icon" d="M543 514 H595"/>
        <path d="M565 492 L565 505 L568 501 L572 507 L574 506 L571 500 L576 500 Z" fill="var(--brand-blue)"/>
      </g>
      <g>
        <circle cx="701" cy="588" r="56" fill="var(--white)" stroke="var(--brand-blue)" stroke-width="7"/>
        <path d="M660 624 L645 648 L672 632 Z" fill="var(--white)"/>
        <text class="node-label" x="701" y="564">Infrastructure</text>
        <text class="node-label" x="701" y="579">Services</text>
        <rect class="icon" x="684" y="592" width="22" height="32"/>
        <path class="icon" d="M689 598h4M697 598h4M689 605h4M697 605h4M689 612h4M697 612h4M706 606h10v18h-10"/>
        <path class="icon" d="M710 612 L722 624 M722 612 L710 624"/>
      </g>
      <g>
        <circle cx="638" cy="732" r="56" fill="var(--white)" stroke="var(--brand-blue)" stroke-width="7"/>
        <path d="M583 740 L560 745 L585 758 Z" fill="var(--white)"/>
        <text class="node-label" x="638" y="713">Application</text>
        <text class="node-label" x="638" y="728">Services</text>
        <path class="icon" d="M638 766 C630 756 626 751 626 745 A12 12 0 0 1 650 745 C650 751 646 756 638 766 Z"/>
        <circle class="icon" cx="638" cy="745" r="4"/>
        <path class="icon" d="M620 768 L646 776 L658 770 L632 762 Z"/>
      </g>
      <g>
        <circle cx="475" cy="730" r="56" fill="var(--white)" stroke="var(--brand-blue)" stroke-width="7"/>
        <path d="M445 688 L455 660 L470 680 Z" fill="var(--white)"/>
        <text class="node-label" x="475" y="706">IT Planning</text>
        <rect class="icon" x="463" y="722" width="34" height="32"/>
        <path class="icon" d="M455 720 V760 M451 724 H459 M470 745 L480 732 L490 740 M476 750 H490"/>
      </g>
      <g>
        <circle cx="431" cy="570" r="56" fill="var(--white)" stroke="var(--brand-blue)" stroke-width="7"/>
        <path d="M474 540 L496 525 L484 560 Z" fill="var(--white)"/>
        <text class="node-label" x="431" y="546">IT</text>
        <text class="node-label" x="431" y="561">Administration</text>
        <rect class="icon" x="420" y="586" width="22" height="8"/>
        <path class="icon" d="M431 594 V606 M410 580 V604 H420 M452 580 V604 H442"/>
      </g>
    </svg>

    <div class="intro-box">
      <h2>You have big plans, right?</h2>
      <p>Technology may help you get there, but how can you plan where you want to go without defining where you are today?</p>
      <hr>
      <h2>We can help!</h2>
      <p>Norvane LLC provides a comprehensive assessment of the technology used to run your business. The documentation and review process delivers the visibility and reassurance you need to protect your business.</p>
      <p>Our team understands that each business operates on its own unique complexities, and crafting a solution requires a custom, unbiased review. Positioning your company with the right insight is intrumental to your success and our goal as your technology partner.</p>
    </div>

    <div class="deliverables-head">Dossier Deliverables</div>
    <ul class="deliverables">
      <li>Executive Dashboard</li>
      <li>Technology Recommendations</li>
      <li>Technology Product Summary</li>
      <li>In-depth Questionnaire</li>
      <li>Recommended IT Policies</li>
      <li>Technology Product Details</li>
      <li>Potential Cost Savings</li>
      <li>Full Infrastructure Detailed Report</li>
    </ul>

    <p class="cta">Take the first step – Call us today!</p>
    <div class="contact-band">
      <strong>Norvane LLC</strong><span class="sep">|</span>866-555-0142<span class="sep">|</span>sales@norvanellc.com<span class="sep">|</span>www.norvanellc.com
    </div>
  </div>
</body>
</html>
```